Flyer-Design für Wohn -und Einrichtungsberaterin
Zielgruppe
Ich bin eine Wohn -und Einrichtungsberaterin und biete neben der Wohnraumopitimierung auch Gartenberatung und Workshops an. Ich bin gelernte Floristin und habe daher einen engen Bezug zur Natürlichkeit.
Aufgabenstellung
Mein Flyer soll die Größe 148 x 148mm haben, mit einer klaren und ruhigen Erscheinung. Das Farbkonzept sollte sich in natürlichen und gedeckten Erdtönen wiederfinden. Trotzdem soll das Konzept ausdrucksstark präsentiert werden.
Vorderseite:
-transparentes Wohnbild im Hintergrund, darauf das Logo
-Bild (Tisch) und Logo siehe Anhänge
Rückseite:
-4 quadratische Textwürfel 2x2 angeordnet (neben- und untereinander)
1. Würfel (oben links)
Überschrift: WOHNRAUMGESTALTUNG
Text: Mit der vorhandenen Einrichtung eine Verbesserung des Wohngefühls schaffen.
2. Würfel (oben rechts)
Überschrift:GARTENBERATUNG
Text: Durch Anregung in der Garten -und Terassengestaltung ein neues Erscheinungsbild kreieren.
3. Würfel (unten links)
Überschrift: RAUMDESIGN
Text: In Praxis- und Gewerberäumen eine neue Atmosphäre erzielen.
4.Würfel (unten rechts)
Überschrift: WORKSHOPS
Text: Kreative Gruppenevents zu verschiedensten Anlässen und Themen erleben.

```html
<!DOCTYPE html>
<html lang="de">
<head>
<meta charset="utf-8">
<title>Hausklang – Flyer</title>
<link rel="stylesheet" href="https://fonts.googleapis.com/css2?family=Jost:wght@400&family=EB+Garamond:wght@400&display=swap">
<style>
  :root {
    --paper: #ffffff;
    --panel-start: #d6cec9;
    --panel-mid: #cbc3bf;
    --panel-end: #b3aca9;
    --ink-heading: #33494a;
    --ink-body: #6e6660;
    --frame-line: #ffffff;
    --logo-ink: #3a4e4f;
  }
  * { margin: 0; padding: 0; box-sizing: border-box; }
  html, body { width: 1200px; height: 629px; overflow: hidden; background: var(--paper); }
  .canvas { position: relative; width: 1200px; height: 629px; }

  .front {
    position: absolute; left: 58px; top: 41px; width: 542px; height: 543px;
    background:
      linear-gradient(180deg, rgba(70,70,72,.55) 0%, rgba(120,110,100,.25) 45%, rgba(230,220,210,.2) 100%),
      linear-gradient(100deg, #6a6d6a 0%, #a58b74 40%, #c9b29a 65%, #e6e2da 100%);
  }
  .logo-frame {
    position: absolute; left: 97px; top: 347px; width: 349px; height: 124px;
    border: 1px solid var(--frame-line);
  }
  .logo-card {
    position: absolute; left: 106px; top: 355px; width: 330px; height: 108px;
    background: var(--paper);
    display: flex; align-items: center; justify-content: center;
  }
  .logo-name {
    font-family: "Jost", sans-serif; font-weight: 400;
    font-size: 40px; letter-spacing: .08em; color: var(--logo-ink);
  }

  .back {
    position: absolute; left: 617px; top: 41px; width: 542px; height: 543px;
    background: linear-gradient(90deg, var(--panel-start) 0%, var(--panel-mid) 55%, var(--panel-end) 100%);
  }
  .tile { position: absolute; width: 219px; height: 219px; border: 1px solid var(--frame-line); }
  .tile-card {
    position: absolute; left: 8px; top: 8px; width: 201px; height: 201px;
    background: var(--paper); padding: 37px 0 0 28px;
  }
  .tile h2 {
    font-family: "Jost", sans-serif; font-weight: 400;
    font-size: 15.5px; line-height: 19px; letter-spacing: .13em;
    color: var(--ink-heading); margin-bottom: 13px;
  }
  .tile p {
    font-family: "EB Garamond", serif; font-size: 12.5px; line-height: 18.2px;
    color: var(--ink-body); width: 170px;
  }
  .tile--1 { left: 39px; top: 39px; }
  .tile--2 { left: 283px; top: 39px; }
  .tile--3 { left: 39px; top: 283px; }
  .tile--4 { left: 283px; top: 283px; }
</style>
</head>
<body>
<div class="canvas">
  <section class="front" role="img" aria-label="Helles, transparentes Wohnbild: Holztisch mit Stühlen, Windlichtern und Vasen in einem Einrichtungsraum">
    <div class="logo-frame"></div>
    <div class="logo-card"><span class="logo-name">Hausklang</span></div>
  </section>

  <section class="back">
    <article class="tile tile--1"><div class="tile-card">
      <h2>WOHNRAUM-<br>GESTALTUNG</h2>
      <p>Mit der vorhandenen Einrichtung eine Verbesse&shy;rung des Wohngefühls schaffen.</p>
    </div></article>
    <article class="tile tile--2"><div class="tile-card">
      <h2>GARTEN-<br>BERATUNG</h2>
      <p>Durch Anregung in der Garten- und Terassen&shy;gestaltung ein neues Erscheinungsbild kreieren.</p>
    </div></article>
    <article class="tile tile--3"><div class="tile-card">
      <h2>RAUMDESIGN</h2>
      <p>In Praxis- und Gewerberäu&shy;men eine neue Atmosphäre erzielen.</p>
    </div></article>
    <article class="tile tile--4"><div class="tile-card">
      <h2>WORKSHOPS</h2>
      <p>Kreative Gruppenevents zu verschiedensten Anlässen und Themen erleben.</p>
    </div></article>
  </section>
</div>
</body>
</html>
```